New Business Card Design Project

Updated business card design. I am moving towards more coaching of, for the most part women, who are searching for more in their lives. I am an intuitive healer, homeopath and nutritionist but also an author and motivational speaker. Int the past I have included my photo on the card but that is not essential. My book is called the Brilliance of Saffron - Reclaiming the Shade of Your Spirit so my colours are typically magenta.
Target Market(s)
Women - 35 - 60 considering improving their health. However, I am also a professional speaker with a target audience including corporate and conferences.
Industry/Entity Type
Health And Wellness
Contact Information for Business Card
Lucinda Parvell, Hom, RHN, BA
www.lucindaparvell.com
lucinda@lucindaparvell.com
519-362-7015
Facebook, instagram and twitter logos
Look and feel
Each slider illustrates characteristics of the customer's brand and the style your logo design should communicate.

```html
<!DOCTYPE html>
<html lang="en">
<head>
<meta charset="utf-8">
<title>Lucinda Parvell – Business Card</title>
<link href="https://fonts.googleapis.com/css2?family=Jost:wght@300;400&family=Josefin+Slab:wght@400;600&display=swap" rel="stylesheet">
<style>
  :root {
    --backdrop: #262626;
    --card: #ececec;
    --ink: #1c1c1c;
    --magenta: #c8285f;
    --band: #d02a62;
    --white: #ffffff;
    --photo-dark: #3a2a24;
    --photo-mid: #b08a78;
  }
  * { box-sizing: border-box; margin: 0; padding: 0; }
  html, body { width: 1200px; height: 1142px; overflow: hidden; }
  body { background: var(--backdrop); position: relative; font-family: "Jost", sans-serif; }

  .card {
    position: absolute; left: 323px; width: 554px; height: 334px;
    background: var(--card); border-radius: 12px; overflow: hidden;
  }
  .card--front { top: 210px; }
  .card--back { top: 597px; }

  .brand-name {
    position: absolute; color: var(--ink); text-align: center;
    font-family: "Jost", sans-serif; font-weight: 300; white-space: nowrap; line-height: 1;
  }
  .card--front .brand-name { left: 0; right: 0; top: 136px; font-size: 56px; }
  .card--back .brand-name { left: 248px; width: 290px; top: 62px; font-size: 32px; }

  .portrait {
    position: absolute; left: 0; top: 0; width: 232px; height: 334px;
    background: linear-gradient(160deg, var(--photo-dark) 0%, var(--photo-mid) 55%, var(--magenta) 100%);
  }

  .contact { position: absolute; right: 22px; text-align: right; color: var(--ink); white-space: nowrap; }
  .contact__name { top: 144px; font-family: "Jost", sans-serif; font-weight: 300; font-size: 22px; line-height: 28px; color: var(--magenta); }
  .contact__credentials { top: 175px; font-family: "Josefin Slab", serif; font-size: 12px; line-height: 14px; }
  .contact__list { top: 211px; right: 22px; list-style: none; font-family: "Josefin Slab", serif; font-size: 15px; }
  .contact__list li { display: flex; align-items: center; justify-content: flex-end; gap: 9px; height: 21px; }
  .contact__list svg { width: 18px; height: 18px; flex: none; }

  .social-band {
    position: absolute; left: 232px; right: 0; bottom: 0; height: 35px;
    background: var(--band); color: var(--white);
    display: flex; align-items: center; padding-left: 80px; gap: 4px;
    font-family: "Josefin Slab", serif; font-size: 16px;
  }
  .social-band__label { margin-right: 6px; }
  .social-band__dot { width: 17px; height: 17px; border-radius: 50%; background: var(--white); }
</style>
</head>
<body>

<section class="card card--front">
  <div class="brand-name">Lucinda Parvell</div>
</section>

<section class="card card--back">
  <div class="portrait" role="img" aria-label="Portrait photo of Lucinda Parvell"></div>

  <div class="brand-name">Lucinda Parvell</div>

  <div class="contact contact__name">Lucinda Parvell</div>
  <div class="contact contact__credentials">Hom, RHN, BA</div>

  <ul class="contact contact__list">
    <li>519-362-7015
      <svg viewBox="0 0 20 20" aria-hidden="true"><circle cx="10" cy="10" r="8.5" fill="none" stroke="var(--ink)" stroke-width="1.2"/><path d="M6 8.5c0-1.5 8-1.5 8 0v1h-2.2v-.8H8.2v.8H6z M7.2 10h5.6l1 4H6.2z" fill="var(--magenta)"/></svg>
    </li>
    <li>www.lucindaparvell.com
      <svg viewBox="0 0 20 20" aria-hidden="true"><circle cx="10" cy="10" r="8.5" fill="none" stroke="var(--ink)" stroke-width="1.2"/><circle cx="10" cy="10" r="4.5" fill="none" stroke="var(--magenta)" stroke-width="1.2"/><path d="M5.5 10h9M10 5.5v9" stroke="var(--magenta)" stroke-width="1"/></svg>
    </li>
    <li>lucinda@lucindaparvell.com
      <svg viewBox="0 0 20 20" aria-hidden="true"><circle cx="10" cy="10" r="8.5" fill="none" stroke="var(--ink)" stroke-width="1.2"/><rect x="5.5" y="7" width="9" height="6" fill="var(--magenta)"/><path d="M5.5 7l4.5 3.5L14.5 7" fill="none" stroke="var(--white)" stroke-width="1"/></svg>
    </li>
  </ul>

  <div class="social-band">
    <span class="social-band__label">Follow us on</span>
    <span class="social-band__dot"></span>
    <span class="social-band__dot"></span>
    <span class="social-band__dot"></span>
  </div>
</section>

</body>
</html>
```